Maplerise Trading Inc. needs an innovative idea for letterhead and visiting cards.

Maplerise Trading Inc. is a Canadian brand since 2007. It is a renown dealer of kids and office furniture locally. Moreover, exporting electric fixtures e.g. switches, LED's, down-lights etc. to Middle East and Africa. We have initiated a number of steps including re-branding, to boost our export in 2020. We have successfully designed our new logo a few months ago through 'Artfolio' and now we are looking for an innovative idea for a letterhead.
Some key points:
• Red, black and white are the three colors used in all our packaging and furniture. (grey is optional)
• Shouldn’t be too wide.
• Use of watermark is preferable.
• You can visit our North American site at www.mapleriseinc.com. Export website of the company will be launched soon. www.mapleriseinc.ca
• Same letterhead will be used locally and internationally.
• Our new logo and sample packaging is attached.

```html
<!DOCTYPE html>
<html lang="en">
<head>
<meta charset="utf-8">
<title>Maplerise Trading Letterhead</title>
<link rel="stylesheet" href="https://fonts.googleapis.com/css2?family=Open+Sans:wght@400&family=Roboto:wght@400;500&family=Montserrat:wght@500&display=swap">
<style>
  :root {
    --backdrop: #cfcfcf;
    --paper: #f6f6f6;
    --brand-red: #940008;
    --ink: #4a4a4a;
    --charcoal: #444446;
    --watermark: rgba(148, 0, 8, 0.06);
  }
  * { box-sizing: border-box; margin: 0; padding: 0; }
  html, body { width: 1200px; height: 1108px; overflow: hidden; background: var(--backdrop); }
  .letterhead {
    position: absolute; left: 227px; top: 24px; width: 746px; height: 1060px;
    background: var(--paper); overflow: hidden;
  }
  .brand {
    position: absolute; left: 0; right: 0; top: 76px;
    display: flex; justify-content: center; align-items: center; gap: 14px;
  }
  .brand-square { width: 56px; height: 56px; background: var(--brand-red); border-radius: 6px; }
  .brand-name {
    font-family: "Montserrat", sans-serif; font-weight: 500; font-size: 27px;
    line-height: 31px; letter-spacing: 1px; color: var(--charcoal); text-transform: uppercase;
  }
  .watermark {
    position: absolute; left: 175px; top: 300px; width: 400px; height: 400px;
    background: var(--watermark); border-radius: 40px;
  }
  .letter-body {
    position: absolute; left: 62px; top: 262px; width: 624px;
    font-family: "Open Sans", sans-serif; font-size: 14.6px; line-height: 20.9px;
    color: var(--ink); text-align: justify;
  }
  .letter-body p { margin-bottom: 20.9px; }
  .signature-area {
    display: block; width: 90px; height: 84px; margin-top: 6px;
    background: linear-gradient(135deg, rgba(0,0,0,0.06), rgba(0,0,0,0.02));
  }
  .contact {
    position: absolute; left: 0; right: 0; top: 975px;
    font-family: "Roboto", sans-serif; font-size: 16.8px; color: var(--ink); text-align: center;
  }
  .contact-address { line-height: 26px; }
  .contact-address .label { color: var(--brand-red); font-weight: 500; }
  .contact-lines { display: flex; justify-content: center; gap: 10px; line-height: 28px; }
  .contact-item { display: inline-flex; align-items: center; gap: 5px; }
  .contact-item svg { width: 14px; height: 14px; }
  .footer-band { position: absolute; left: 0; right: 0; bottom: 0; height: 10px; display: flex; gap: 2px; }
  .footer-band .red { flex: 1; background: var(--brand-red); }
  .footer-band .grey { flex: 1; background: var(--charcoal); }
</style>
</head>
<body>
  <main class="letterhead">
    <header class="brand">
      <span class="brand-square"></span>
      <span class="brand-name">Maplerise<br>Trading</span>
    </header>

    <div class="watermark"></div>

    <section class="letter-body">
      <p>Dear customer,</p>
      <p>Lorem ipsum dolor sit amet, consectetur adipisicing elit, sed do eiusmod tempor incididunt ut labore et dolore magna aliqua. Ut enim ad minim veniam, quis nostrud exercitation ullamco laboris nisi ut aliquip ex ea commodo consequat. Duis aute irure dolor in reprehenderit in voluptate velit esse cillum dolore eu fugiat nulla pariatur. Excepteur sint occaecat cupidatat non proident, sunt in culpa qui officia deserunt mollit anim id est laborum.</p>
      <p>Lorem ipsum dolor sit amet, consectetur adipisicing elit, sed do eiusmod tempor incididunt ut labore et dolore magna aliqua. Ut enim ad minim veniam, quis nostrud exercitation ullamco laboris nisi ut aliquip ex ea commodo consequat. Duis aute irure dolor in reprehenderit in voluptate velit esse cillum dolore eu fugiat nulla pariatur. Excepteur sint occaecat cupidatat non proident, sunt in culpa qui officia deserunt mollit anim id est laborum.</p>
      <p>Lorem ipsum dolor sit amet, consectetur adipisicing elit, sed do eiusmod tempor incididunt ut labore et dolore magna aliqua. Ut enim ad minim veniam, quis nostrud exercitation ullamco laboris nisi ut aliquip ex ea commodo consequat. Duis aute irure dolor in reprehenderit in voluptate velit esse cillum dolore eu fugiat nulla pariatur. Excepteur sint occaecat cupidatat non proident, sunt in culpa qui officia deserunt mollit anim id est laborum.</p>
      <p>Lorem ipsum dolor sit amet, consectetur adipisicing elit, sed do eiusmod tempor incididunt ut labore et dolore magna aliqua. Ut enim ad minim veniam, quis nostrud exercitation ullamco laboris nisi ut aliquip ex ea commodo consequat. Duis aute irure dolor in reprehenderit.</p>
      <p style="margin-bottom:0">Yours Sincerely,</p>
      <span class="signature-area" role="img" aria-label="Handwritten signature of the sender"></span>
    </section>

    <footer class="contact">
      <div class="contact-address"><span class="label">Address:</span> 48 Birchwood Ave, Unit 210, Markham, ON L3R 2K9</div>
      <div class="contact-lines">
        <span class="contact-item">
          <svg viewBox="0 0 14 14" aria-hidden="true"><rect width="14" height="14" rx="2" fill="#940008"/><path d="M4 3.2l1.6-.4 1 2.2-1 .8a5 5 0 0 0 2.6 2.6l.8-1 2.2 1-.4 1.6C8 10.5 3.5 6 4 3.2z" fill="#fff"/></svg>
          +1 (888) 420-3175
        </span>
        <span class="contact-item">
          <svg viewBox="0 0 14 14" aria-hidden="true"><rect width="14" height="14" rx="2" fill="#940008"/><rect x="3" y="4" width="8" height="6" fill="none" stroke="#fff" stroke-width="1.2"/><path d="M3 4l4 3.2L11 4" fill="none" stroke="#fff" stroke-width="1.2"/></svg>
          info@mapleriseinc.com
        </span>
        <span class="contact-item">
          <svg viewBox="0 0 14 14" aria-hidden="true"><rect width="14" height="14" rx="2" fill="#940008"/><circle cx="7" cy="7" r="4" fill="none" stroke="#fff" stroke-width="1.1"/><path d="M3 7h8M7 3c-2 2.4-2 5.6 0 8M7 3c2 2.4 2 5.6 0 8" fill="none" stroke="#fff" stroke-width="0.9"/></svg>
          www.mapleriseinc.com
        </span>
      </div>
    </footer>

    <div class="footer-band"><span class="red"></span><span class="grey"></span></div>
  </main>
</body>
</html>
```